依頼詳細
・B4、両面カラー
・明るく楽しい雰囲気、お客様に安心感・信頼が伝わるようなイメージ。
(安っぽくならないようにご注意ください。お願いします。
・画像使用の場合は、制作者様側でご用意ください。
・オプションの習いごと3つの詳細を掲載ください。
(名前・ロゴ・詳細・写真はご依頼確定後にお渡しいたします。)
・来年度募集「キャンペーン」をもとに説明会に参加、スクール入会したくなるようなチラシにしていただきたいです。
記載項目
社名/電話番号/URL/メールアドレス/住所/キャッチコピー/料金/学童のポイント/学童内容/習い紹介//キャンペーン情報/イベント&説明会情報/

※その他詳細は添付ファイルPDFをご確認下さい。
サイズ
B4
ページ数
両面
希望イメージ
シンプル 複雑
単色 カラフル
暗い 明るい
日常 高級
遊び心 厳粛
未来的 伝統的
女性的 男性的
希望する色
水色系、緑系、黄・オレンジ系
納品ファイル
• 高解像度JPG (.jpg)
• イラストレーター形式 (.ai)
• PNG形式 (.png)
補足説明
詳細内容は指示書に記載しました。恐れ入りますがご確認ください。
その他弊社HPも参考にご確認ください。https://www.hoshizora-gakudo.jp/
■ 選んだ理由

イラストや図形を使って、可愛らしくもありながら信頼や安心感も伝わるデザインであり、今回私たちが求めるデザインに最も近いと思いました。お客様に伝えたい情報や、スクールの様子などが最も伝わる構成でもあり、当選させていただきました。
また、こちらからの加筆修正に対するレスポンスの早さと丁寧な対応を通じて、デザイナーさんの誠実さを感じられたのも当選理由の一つです。

■ 提案者全員のお礼・コメント

この度はコンペにご参加・ご提出していただき、誠にありがとうございました。
デザイナー様の提案内容と共に、ご提出いただいた案全て、慎重に拝見させていただきました。どの案もとても素晴らしく、一つに絞るのがとても大変でした。

今回ご提出いただいたデザイナーの皆さまに改めて心より感謝申し上げます。
また、コンペを開催した際にはぜひ提案いただけますと幸いです。今後とも、どうぞ宜しくお願い致します。

```html
<!DOCTYPE html>
<html lang="ja">
<head>
<meta charset="utf-8">
<title>HOSHIZORAキッズ 2024年度 学童入会員募集</title>
<link rel="stylesheet" href="https://fonts.googleapis.com/css2?family=M+PLUS+Rounded+1c:wght@500;700;800;900&family=Zen+Maru+Gothic:wght@500;700;900&display=swap">
<style>
  :root{
    --cyan:#17b1e3;
    --cyan-dark:#0b8fc4;
    --orange:#f2861c;
    --orange-light:#ffb347;
    --red:#e8483a;
    --green:#6fbb3b;
    --pink:#ef6a9a;
    --yellow-bg:#fff5c9;
    --cream:#fffbea;
    --ink:#3b3b3b;
    --grey:#8a8a8a;
    --white:#ffffff;
  }
  *{box-sizing:border-box;margin:0;padding:0}
  html,body{width:846px;height:1200px;overflow:hidden}
  body{font-family:"M PLUS Rounded 1c",sans-serif;color:var(--ink);background:var(--white)}
  .flyer{position:relative;width:846px;height:1200px;background:var(--white);overflow:hidden}

  /* header over a soft room backdrop */
  .hero-photo{position:absolute;top:0;left:0;width:846px;height:332px;
    background:
      radial-gradient(ellipse 520px 120px at 50% 270px, rgba(232,170,128,.55), rgba(232,170,128,0) 70%),
      linear-gradient(180deg,#f7fbfd 0%,#eef6fb 38%,#d6ebf7 56%,#f2d3b8 78%,#e9b996 100%)}
  .brand{position:absolute;top:34px;left:0;width:100%;text-align:center;font-weight:900;font-size:66px;letter-spacing:2px;color:var(--cyan);line-height:1}
  .tagline{position:absolute;top:118px;left:0;width:100%;text-align:center;font-family:"Zen Maru Gothic",sans-serif;font-weight:700;font-size:30px;letter-spacing:3px;color:var(--cyan-dark)}
  .tagline b{color:var(--orange)}

  /* campaign */
  .campaign{position:absolute;top:332px;left:0;width:846px;height:142px;background:var(--yellow-bg)}
  .recruit-pill{position:absolute;top:-18px;left:50%;transform:translateX(-50%);background:var(--cyan);color:var(--white);font-weight:800;font-size:25px;padding:6px 46px;border-radius:30px;white-space:nowrap}
  .early{position:absolute;top:34px;left:40px;width:250px;text-align:center;color:var(--orange);font-weight:900;line-height:1.1}
  .early .big{font-size:48px;letter-spacing:6px}
  .early .sub{font-size:38px;letter-spacing:1px}
  .confetti{position:absolute;top:28px;left:30px}
  .price{position:absolute;top:30px;left:310px;width:500px}
  .price .regular{font-weight:800;font-size:28px;color:var(--orange);text-decoration:line-through;text-decoration-thickness:3px;padding-left:40px}
  .price .arrow{position:absolute;top:22px;left:0}
  .price .free{position:absolute;top:26px;left:90px;font-weight:900;color:var(--orange);font-size:46px;white-space:nowrap}
  .price .free em{font-style:normal;font-size:98px;line-height:1;vertical-align:-10px;margin-left:6px}

  /* section headings */
  .section-title{position:absolute;left:0;width:100%;text-align:center;font-weight:900;font-size:34px;letter-spacing:4px}
  .features-title{top:480px;color:var(--white);-webkit-text-stroke:7px var(--cyan);paint-order:stroke fill}
  .events-title{top:722px;color:var(--orange)}
  .events-title .amp{color:var(--cyan);margin:0 6px}

  /* features */
  .features{position:absolute;top:534px;left:28px;width:790px;display:flex;gap:14px}
  .feature{flex:1;text-align:center}
  .feature-photo{height:118px;border-radius:10px;background:linear-gradient(160deg,#dfe9f2,#b9cbd9)}
  .feature:nth-child(2) .feature-photo{background:linear-gradient(160deg,#f2ece2,#d9cbb6)}
  .feature:nth-child(3) .feature-photo{background:linear-gradient(160deg,#f4efe4,#e3d2b8)}
  .feature:nth-child(4) .feature-photo{background:linear-gradient(160deg,#e6f1ea,#bcd8c8)}
  .feature p{margin-top:8px;font-weight:700;font-size:14px;line-height:1.35;color:var(--ink)}

  /* events */
  .events{position:absolute;top:770px;left:28px;width:790px;display:flex;gap:12px}
  .event{flex:1;background:var(--cream);border-radius:12px;padding:12px 12px 14px;height:210px}
  .event-head{display:flex;align-items:center;gap:8px}
  .month{flex:none;width:62px;height:46px;border-radius:8px;color:var(--white);font-weight:900;font-size:26px;display:flex;align-items:center;justify-content:center}
  .month small{font-size:16px}
  .event:nth-child(1) .month{background:var(--orange)}
  .event:nth-child(2) .month{background:var(--green)}
  .event:nth-child(3) .month{background:var(--red)}
  .event-name{font-weight:900;font-size:19px;line-height:1.25;color:var(--ink)}
  .event ul{list-style:none;margin-top:12px;font-size:13px;line-height:1.7;font-weight:500}
  .event li::before{content:"";display:inline-block;width:7px;height:7px;border-radius:50%;background:var(--cyan);margin-right:6px;vertical-align:1px}

  /* schools */
  .schools{position:absolute;top:1000px;left:28px;width:790px;display:flex;gap:14px}
  .school{flex:1;height:172px;border:2px solid var(--cyan);border-radius:10px;position:relative;overflow:hidden;background:var(--white)}
  .school-name{background:var(--cyan);color:var(--white);font-weight:800;font-size:17px;padding:6px 12px}
  .school-address{font-size:10.5px;line-height:1.5;padding:6px 12px 0;width:250px;color:var(--grey);white-space:nowrap}
  .school-phone{display:flex;align-items:center;gap:6px;padding:6px 12px 0;font-weight:900;font-size:30px;color:var(--ink)}
  .school-hours{padding:6px 12px 0;font-size:12px;font-weight:500;color:var(--ink)}
  .school-photo{position:absolute;right:10px;top:42px;width:120px;height:96px;border-radius:6px;background:linear-gradient(160deg,#e7eef4,#c4d3df)}
  .site{position:absolute;bottom:6px;left:0;width:100%;text-align:center;font-size:12px;font-weight:700;color:var(--cyan-dark)}
</style>
</head>
<body>
<main class="flyer">
  <div class="hero-photo" role="img" aria-label="明るい教室で笑顔でポーズをとる子どもたちの写真"></div>

  <header>
    <h1 class="brand">HOSHIZORAキッズ</h1>
    <p class="tagline">あたま・からだ・こころを育む <b>学童保育</b></p>
  </header>

  <section class="campaign">
    <div class="recruit-pill">2024年度 学童入会員募集スタート！</div>
    <svg class="confetti" width="270" height="110" viewBox="0 0 270 110" aria-hidden="true">
      <rect x="6" y="8" width="8" height="14" rx="2" fill="#ef6a9a" transform="rotate(-20 10 15)"/>
      <rect x="250" y="4" width="8" height="14" rx="2" fill="#6fbb3b" transform="rotate(25 254 11)"/>
      <circle cx="10" cy="96" r="5" fill="#17b1e3"/>
      <circle cx="262" cy="92" r="5" fill="#ffb347"/>
    </svg>
    <div class="early">
      <div class="big">早割</div>
      <div class="sub">キャンペーン</div>
    </div>
    <div class="price">
      <div class="regular">通常22,000円</div>
      <svg class="arrow" width="80" height="70" viewBox="0 0 80 70" aria-hidden="true">
        <path d="M10 6 V44 H58" fill="none" stroke="#17b1e3" stroke-width="9" stroke-linecap="round" stroke-linejoin="round"/>
        <path d="M52 30 L72 44 L52 58 Z" fill="#17b1e3"/>
      </svg>
      <div class="free">入会金<em>0</em>円</div>
    </div>
  </section>

  <h2 class="section-title features-title">スクールの特長</h2>
  <section class="features">
    <div class="feature">
      <div class="feature-photo" role="img" aria-label="送迎用のマイクロバスの写真"></div>
      <p>ご自宅付近まで送迎サポート</p>
    </div>
    <div class="feature">
      <div class="feature-photo" role="img" aria-label="宿題に取り組む子どもの写真"></div>
      <p>宿題・学習サポート</p>
    </div>
    <div class="feature">
      <div class="feature-photo" role="img" aria-label="料理体験をする子どもの手元の写真"></div>
      <p>月1回の料理体験も可能</p>
    </div>
    <div class="feature">
      <div class="feature-photo" role="img" aria-label="タブレットで学ぶ子どもの写真"></div>
      <p>STEAM教育を活用した<br>オリジナルのカリキュラム</p>
    </div>
  </section>

  <h2 class="section-title events-title">イベント<span class="amp">&amp;</span>説明会日程</h2>
  <section class="events">
    <article class="event">
      <div class="event-head"><div class="month">10<small>月</small></div><div class="event-name">学童説明会</div></div>
      <ul>
        <li>10月14日 みなみ公園前</li>
        <li>10月21日 あさひ台中央</li>
        <li>各回 10:00〜11:30</li>
        <li>要予約・参加無料</li>
      </ul>
    </article>
    <article class="event">
      <div class="event-head"><div class="month">11<small>月</small></div><div class="event-name">秋の体験フェス&amp;<br>学童体験・説明会</div></div>
      <ul>
        <li>11月11日 みなみ公園前</li>
        <li>11月18日 あさひ台中央</li>
        <li>工作・ゲームを体験</li>
      </ul>
    </article>
    <article class="event">
      <div class="event-head"><div class="month">12<small>月</small></div><div class="event-name">クリスマス会&amp;<br>学童体験・説明会</div></div>
      <ul>
        <li>12月9日 あさひ台中央</li>
        <li>12月16日 みなみ公園前</li>
        <li>プレゼント交換あり</li>
      </ul>
    </article>
  </section>

  <section class="schools">
    <div class="school">
      <div class="school-name">HOSHIZORAキッズ みなみ公園前</div>
      <p class="school-address">〒100-0000 東京都みなみ区公園前1-2-3<br>みなみ公園前ビル2階</p>
      <div class="school-phone">
        <svg width="24" height="24" viewBox="0 0 24 24" aria-hidden="true"><path d="M6.6 10.8a15 15 0 0 0 6.6 6.6l2.2-2.2a1 1 0 0 1 1-.25 11.4 11.4 0 0 0 3.6.57 1 1 0 0 1 1 1V20a1 1 0 0 1-1 1A17 17 0 0 1 3 4a1 1 0 0 1 1-1h3.5a1 1 0 0 1 1 1c0 1.25.2 2.45.57 3.57a1 1 0 0 1-.25 1z" fill="#17b1e3"/></svg>
        03-5550-1824
      </div>
      <p class="school-hours">営業時間 月〜金 11時〜20時</p>
      <div class="school-photo" role="img" aria-label="みなみ公園前教室の室内写真"></div>
    </div>
    <div class="school">
      <div class="school-name">HOSHIZORAキッズ あさひ台中央</div>
      <p class="school-address">〒240-0000 神奈川県あさひ台市中央4-5-6<br>あさひ台ビル3階</p>
      <div class="school-phone">
        <svg width="24" height="24" viewBox="0 0 24 24" aria-hidden="true"><path d="M6.6 10.8a15 15 0 0 0 6.6 6.6l2.2-2.2a1 1 0 0 1 1-.25 11.4 11.4 0 0 0 3.6.57 1 1 0 0 1 1 1V20a1 1 0 0 1-1 1A17 17 0 0 1 3 4a1 1 0 0 1 1-1h3.5a1 1 0 0 1 1 1c0 1.25.2 2.45.57 3.57a1 1 0 0 1-.25 1z" fill="#17b1e3"/></svg>
        046-555-3071
      </div>
      <p class="school-hours">営業時間 月〜金 11時〜20時</p>
      <div class="school-photo" role="img" aria-label="あさひ台中央教室の室内写真"></div>
    </div>
  </section>
  <p class="site">https://www.hoshizora-gakudo.jp/</p>
</main>
</body>
</html>
```